LUMO Electrical Services Letter Head

I need a professional clean looking design that will incorporate my company logo and information such as postal address, website, contact email "service@lumoelectrical.com.au" and phone number.

somewhere on the document i will also require my electrical contractor number "EC 047362" and my Australian Business number "57 193 640 208" these have to legally be on the document so they dont need to be a main feature, maybe in the footer in a smaller text.

Can you also have the 3 blue dashes from my logo as the watermark.

I would like the colour scheme to match my logo, business card and website www.lumoelectrical.com.au

I have the JPEG and PNG files for my logo which it will not allow me to upload as they are too wide, if you require these please let me know.

Target Market(s)

To be used for quotes and letters to commercial clients

Industry/Entity Type

Electric Company

Colors
0555a3
3176b5
85acd3
cfdfed
eaf1f7

Requirements
Must have
• company logo and information such as postal address, website, contact email "service@lumoelectrical.com.au" and phone number.
• somewhere on the document i will also require my electrical contractor number "EC 047362" and my Australian Business number "57 193 640 208" these have to legally be on the document so they dont need to be a main feature, maybe in the footer in a smaller text.
• I would like the colour scheme to match my logo, business card and website www.lumoelectrical.com.au
Nice to have
• Can you also have the 3 blue dashes from my logo as the watermark.

```html
<!DOCTYPE html>
<html lang="en">
<head>
<meta charset="utf-8">
<title>LUMO Electrical Services Letterhead</title>
<link href="https://fonts.googleapis.com/css2?family=Noto+Sans:wght@400;700&display=swap" rel="stylesheet">
<style>
  :root {
    --backdrop: #d4d4d4;
    --paper: #ffffff;
    --ink: #232323;
    --brand-deep: #0555a3;
    --brand-mid: #3176b5;
    --brand-soft: #85acd3;
    --brand-pale: #cfdfed;
    --brand-mist: #eaf1f7;
    --art-core: #fbfbfb;
    --art-grey: #ebebed;
  }
  * { margin: 0; padding: 0; box-sizing: border-box; }
  html, body {
    width: 900px; height: 1200px; overflow: hidden;
    background: var(--backdrop);
    font-family: "Noto Sans", Verdana, sans-serif;
    color: var(--ink);
  }
  .letterhead {
    position: absolute; left: 24px; top: 26px;
    width: 853px; height: 1105px;
    background: var(--paper);
    overflow: hidden;
  }
  .brand {
    position: absolute; left: 60px; top: 78px;
    display: flex; align-items: center; gap: 12px;
  }
  .brand-mark {
    width: 22px; height: 22px; background: var(--brand-deep);
  }
  .brand-name {
    font-size: 26px; font-weight: 700; color: var(--ink);
  }
  .contact {
    position: absolute; right: 60px; top: 62px;
    text-align: right; font-size: 15px; font-weight: 700;
    font-style: normal; line-height: 17px; letter-spacing: 0.3px;
    color: var(--ink);
  }
  .background-art {
    position: absolute; left: -124px; top: 114px;
    width: 900px; height: 900px;
    background: radial-gradient(circle closest-side at 50% 50%,
      var(--art-core) 0%,
      #f8f8f9 45%,
      var(--art-grey) 70%,
      #f3f3f4 84%,
      rgba(255,255,255,0) 100%);
  }
  .accent-band {
    position: absolute; left: 406px; top: 474px;
    width: 447px; height: 158px;
    background: linear-gradient(90deg,
      rgba(234,241,247,0) 0%,
      var(--brand-mist) 20%,
      #e1ecf7 55%,
      #dbe2f2 100%);
  }
  .legal {
    position: absolute; left: 0; right: 0; top: 1034px;
    text-align: center; font-size: 12.5px; font-weight: 400;
    color: var(--ink);
  }
</style>
</head>
<body>
  <main class="letterhead">
    <div class="background-art" role="img" aria-label="Faint technical illustration of gears, circuit lines and circular arrows"></div>
    <div class="accent-band" role="img" aria-label="Pale blue brand watermark band"></div>

    <header>
      <div class="brand">
        <span class="brand-mark"></span>
        <span class="brand-name">LUMO Electrical Services</span>
      </div>
      <address class="contact">
        P.O Box 8316, Harlow Park, WA 6174<br>
        Phone: (08) 6120 4759<br>
        Email: service@lumoelectrical.com.au
      </address>
    </header>

    <footer class="legal">ABN 57 193 640 208 | EC 047362</footer>
  </main>
</body>
</html>
```